Edit of business card / magnet

Hi there
Can you please edit the attached business card which I am going to use to print on a magnet. Can you please edit the following:
1) Make it 54 x 90mm with a 3 mm bleed.
2) I need 3 different versions. Each version will be the same with the exception of the following sentence which I need added underneath the Kestrelford Plumbing Services Pty Limited logo:
i) Your local Cherrybrook plumber
ii) Your local Wahroonga plumber
iii) Your local St Ives plumber
3) Can you add the wording "Present this card to receive a $50 discount" somewhere
4) On the right hand side where it lists the different types of services can you add a point "we can work within your budget"
Thanks

```html
<!DOCTYPE html>
<html lang="en">
<head>
<meta charset="utf-8">
<title>Kestrelford Plumbing – Suburb Magnet Cards</title>
<link rel="stylesheet" href="https://fonts.googleapis.com/css2?family=Lato:wght@400;700;900&display=swap">
<style>
  :root {
    --brand-blue: #1a74c4;
    --brand-blue-deep: #136ab6;
    --ink: #1d1d1b;
    --grey: #8a8b8d;
    --paper: #ffffff;
    --backdrop: #e9ebee;
    --badge: #c9a94a;
  }
  * { box-sizing: border-box; margin: 0; padding: 0; }
  html, body {
    width: 1200px; height: 800px; overflow: hidden;
    background: var(--backdrop);
    font-family: "Lato", sans-serif;
  }
  .sheet { position: relative; width: 1200px; height: 800px; }

  .card {
    position: absolute;
    width: 560px; height: 336px;
    background: var(--paper);
    overflow: hidden;
    box-shadow: 0 2px 10px rgba(0,0,0,0.12);
  }
  .card--cherrybrook { left: 30px;  top: 50px; }
  .card--wahroonga   { left: 610px; top: 50px; }
  .card--st-ives     { left: 320px; top: 420px; }

  .card__services-panel {
    position: absolute; top: 0; right: 0; bottom: 0;
    width: 310px;
    background: var(--brand-blue);
  }

  .brand {
    position: absolute; left: 34px; top: 46px;
    display: flex; align-items: flex-start; gap: 10px;
  }
  .brand__mark {
    width: 18px; height: 18px; margin-top: 6px;
    background: var(--brand-blue);
  }
  .brand__name {
    color: var(--brand-blue);
    font-weight: 900;
    line-height: 0.95;
  }
  .brand__name-main { display: block; font-size: 34px; letter-spacing: -0.5px; }
  .brand__name-legal { display: block; font-size: 13px; margin-top: 6px; letter-spacing: 0.5px; text-transform: uppercase; }

  .locale {
    position: absolute; left: 62px; top: 168px;
    color: var(--grey);
  }
  .locale__lead { font-size: 14px; display: block; }
  .locale__suburb {
    display: block; color: var(--brand-blue);
    font-size: 28px; font-weight: 900; line-height: 1.05; margin-left: 10px;
  }
  .locale__tail { display: block; font-size: 13px; text-align: right; }
  .locale--inline .locale__lead,
  .locale--inline .locale__suburb,
  .locale--inline .locale__tail { display: inline; margin-left: 0; }
  .locale--inline { top: 190px; left: 40px; white-space: nowrap; }

  .services {
    position: absolute; right: 34px; top: 40px;
    list-style: none; text-align: right;
    color: var(--paper); font-size: 15px; line-height: 1.25;
    text-transform: uppercase; letter-spacing: 0.3px;
  }
  .services__budget { margin-top: 14px; }

  .contact {
    position: absolute; right: 34px; top: 214px;
    text-align: right; color: var(--paper);
    font-size: 11.5px; line-height: 1.45;
  }
  .contact__licence { font-size: 9px; }
  .contact__phone { font-size: 16px; font-weight: 700; line-height: 1.1; }

  .offer {
    position: absolute; left: 0; right: 0; bottom: 14px;
    display: flex; align-items: center;
    font-size: 10px; font-weight: 700; letter-spacing: 4.2px; text-transform: uppercase;
  }
  .offer__badge {
    width: 18px; height: 18px; margin: 0 10px 0 20px;
    border-radius: 3px; background: var(--badge);
  }
  .offer__start { width: 222px; color: var(--ink); white-space: nowrap; }
  .offer__end { padding-left: 6px; color: var(--paper); white-space: nowrap; }
</style>
</head>
<body>
<main class="sheet">

  <article class="card card--cherrybrook">
    <div class="card__services-panel"></div>
    <div class="brand">
      <span class="brand__mark"></span>
      <p class="brand__name"><span class="brand__name-main">Kestrelford<br>Plumbing</span><span class="brand__name-legal">Services Pty Limited</span></p>
    </div>
    <p class="locale"><span class="locale__lead">Your local</span><span class="locale__suburb">Cherrybrook</span><span class="locale__tail">plumber.</span></p>
    <ul class="services">
      <li>Plumbing Services</li><li>Hot Water Systems</li><li>Gas Services</li><li>Blocked Drains</li><li>Taps Toilets</li>
      <li class="services__budget">We can work<br>within your budget</li>
    </ul>
    <address class="contact">
      <span>enquiry@kestrelfordplumbing.com.au</span><br>
      <span class="contact__licence">Lic #318207c</span><br>
      <span class="contact__phone">0412 555 019</span><br>
      <span>www.kestrelfordplumbing.com.au</span>
    </address>
    <p class="offer"><span class="offer__badge"></span><span class="offer__start">Present this card to</span><span class="offer__end">receive a $50 discount</span></p>
  </article>

  <article class="card card--wahroonga">
    <div class="card__services-panel"></div>
    <div class="brand">
      <span class="brand__mark"></span>
      <p class="brand__name"><span class="brand__name-main">Kestrelford<br>Plumbing</span><span class="brand__name-legal">Services Pty Limited</span></p>
    </div>
    <p class="locale"><span class="locale__lead">Your local</span><span class="locale__suburb">Wahroonga</span><span class="locale__tail">plumber.</span></p>
    <ul class="services">
      <li>Plumbing Services</li><li>Hot Water Systems</li><li>Gas Services</li><li>Blocked Drains</li><li>Taps Toilets</li>
      <li class="services__budget">We can work<br>within your budget</li>
    </ul>
    <address class="contact">
      <span>enquiry@kestrelfordplumbing.com.au</span><br>
      <span class="contact__licence">Lic #318207c</span><br>
      <span class="contact__phone">0412 555 019</span><br>
      <span>www.kestrelfordplumbing.com.au</span>
    </address>
    <p class="offer"><span class="offer__badge"></span><span class="offer__start">Present this card to</span><span class="offer__end">receive a $50 discount</span></p>
  </article>

  <article class="card card--st-ives">
    <div class="card__services-panel"></div>
    <div class="brand">
      <span class="brand__mark"></span>
      <p class="brand__name"><span class="brand__name-main">Kestrelford<br>Plumbing</span><span class="brand__name-legal">Services Pty Limited</span></p>
    </div>
    <p class="locale locale--inline"><span class="locale__lead">Your local </span><span class="locale__suburb">St Ives</span><span class="locale__tail"> plumber.</span></p>
    <ul class="services">
      <li>Plumbing Services</li><li>Hot Water Systems</li><li>Gas Services</li><li>Blocked Drains</li><li>Taps Toilets</li>
      <li class="services__budget">We can work<br>within your budget</li>
    </ul>
    <address class="contact">
      <span>enquiry@kestrelfordplumbing.com.au</span><br>
      <span class="contact__licence">Lic #318207c</span><br>
      <span class="contact__phone">0412 555 019</span><br>
      <span>www.kestrelfordplumbing.com.au</span>
    </address>
    <p class="offer"><span class="offer__badge"></span><span class="offer__start">Present this card to</span><span class="offer__end">receive a $50 discount</span></p>
  </article>

</main>
</body>
</html>
```